business card design for luxurious real estate brand

using the attached logo, i am looking for a 2-sided business card design. the back should be the gold logo on black background. the front needs to include: gold logo, name, phone, email, and website

Industry/Entity Type

real estate

Contact Information for Business Card

logo, name, email, phone, website

Font styles to use
Sans Serif

```html
<!DOCTYPE html>
<html lang="en">
<head>
<meta charset="utf-8">
<title>Casa Aurora – Business Card</title>
<link href="https://fonts.googleapis.com/css2?family=Montserrat:wght@400;500;700&display=swap" rel="stylesheet">
<style>
  :root {
    --backdrop: #3a3a3a;
    --card: #171717;
    --card-deep: #0d0d0d;
    --card-sheen: #2c2c2c;
    --gold: #f7c600;
    --ink-light: #e8e8e8;
  }
  * { margin: 0; padding: 0; box-sizing: border-box; }
  html, body {
    width: 1200px; height: 801px; overflow: hidden;
    background: var(--backdrop);
    font-family: "Montserrat", sans-serif;
  }
  .stage {
    position: relative; width: 1200px; height: 801px;
    display: flex; align-items: center; justify-content: center; gap: 60px;
  }
  .card {
    position: relative; width: 500px; height: 286px;
    background: var(--card);
    border: 1.5px solid var(--gold);
    overflow: hidden;
  }
  /* Front */
  .card-front { display: flex; align-items: center; }
  .brand-block {
    width: 250px; display: flex; flex-direction: column; align-items: center; gap: 14px;
  }
  .brand-mark { width: 22px; height: 22px; background: var(--gold); }
  .brand-name {
    color: var(--gold); font-weight: 500; font-size: 19px;
    letter-spacing: 0.32em; text-transform: uppercase;
  }
  .divider { width: 1.5px; height: 90px; background: var(--gold); }
  .contact-block { padding-left: 28px; }
  .person-name {
    color: var(--gold); font-weight: 700; font-size: 17px;
    text-transform: uppercase; letter-spacing: 0.02em;
  }
  .person-title { color: var(--ink-light); font-size: 13px; margin-bottom: 14px; }
  .contact-list { list-style: none; }
  .contact-list li {
    display: flex; align-items: center; gap: 8px;
    color: var(--ink-light); font-size: 12px; line-height: 1.6;
  }
  .contact-list svg { width: 10px; height: 10px; fill: var(--gold); flex: none; }
  /* Back */
  .card-back { display: flex; align-items: flex-end; justify-content: flex-end; }
  .back-pattern {
    position: absolute; inset: 0;
    background: linear-gradient(120deg, var(--card-deep) 0%, var(--card) 50%, var(--card-sheen) 100%);
  }
  .back-brand {
    position: relative; margin: 0 70px 90px 0;
    display: flex; align-items: center; gap: 10px;
  }
  .back-brand .brand-mark { width: 16px; height: 16px; }
  .back-brand .brand-name { font-size: 16px; }
</style>
</head>
<body>
<main class="stage">
  <section class="card card-front" aria-label="Card front">
    <div class="brand-block">
      <span class="brand-mark"></span>
      <span class="brand-name">Casa Aurora</span>
    </div>
    <span class="divider"></span>
    <div class="contact-block">
      <p class="person-name">Marc Delorme</p>
      <p class="person-title">President</p>
      <ul class="contact-list">
        <li><svg viewBox="0 0 10 10"><path d="M2 0.5 L3.8 2.6 L2.9 3.8 Q4 6 6.2 7.1 L7.4 6.2 L9.5 8 L8.2 9.5 Q2.5 9 0.5 1.8 Z"/></svg>555-014-2290</li>
        <li><svg viewBox="0 0 10 10"><path d="M0 2 H10 V8.5 H0 Z M0.8 2.6 L5 5.6 L9.2 2.6" stroke="#171717" stroke-width="0.8"/></svg>marc@casaaurora.com</li>
        <li><svg viewBox="0 0 10 10"><circle cx="5" cy="5" r="4.5"/><path d="M0.5 5 H9.5 M5 0.5 Q2.5 5 5 9.5 M5 0.5 Q7.5 5 5 9.5" stroke="#171717" stroke-width="0.7" fill="none"/></svg>www.casaaurora.com</li>
      </ul>
    </div>
  </section>

  <section class="card card-back" aria-label="Card back">
    <div class="back-pattern" role="img" aria-label="Repeating embossed brand pattern in gloss black on matte black"></div>
    <div class="back-brand">
      <span class="brand-mark"></span>
      <span class="brand-name">Casa Aurora</span>
    </div>
  </section>
</main>
</body>
</html>
```